new business card, with new logo. Looking for full design

I would like to have a graphic designer/artist create a high standard, premium business logo and business card design that I can either use to print on my own or have printed through them as well. Also, would be nice if I could customize with new employee names and info afterwards. Also, though I don't have a logo, something that matches the theme here https://larkfieldstrategyadvisors.com/ as well as incorporates the letter "M" is what I am currently thinking. Thanks!

Target Market(s)

High end corporate executives

Industry/Entity Type

Economics

Contact Information for Business Card

Dr. Oscar Teodoro-Lindqvist
Principal Advisor
OTL@LarkfieldStrategyAdvisors.com
other contact/website details from here: https://larkfieldstrategyadvisors.com/

Logo Text

Larkfield Strategy Advisors

```html
<!DOCTYPE html>
<html lang="en">
<head>
<meta charset="utf-8">
<title>Larkfield Strategy Advisors — Business Card</title>
<link rel="stylesheet" href="https://fonts.googleapis.com/css2?family=EB+Garamond:wght@400;500&display=swap">
<style>
  :root {
    --stage: #1a1a1a;
    --stage-light: #2c2c2c;
    --card: #2a2a2a;
    --rose: #c8928a;
    --taupe: #5f5249;
    --ink-light: #f2eeea;
    --rule: #5a5654;
  }
  * { box-sizing: border-box; margin: 0; padding: 0; }
  html, body { width: 1200px; height: 1015px; overflow: hidden; }
  body {
    background: radial-gradient(ellipse at 50% 45%, var(--stage-light) 0%, var(--stage) 70%);
    font-family: "EB Garamond", Georgia, serif;
    position: relative;
  }
  .card {
    position: absolute;
    left: 290px;
    width: 620px;
    height: 354px;
    background: var(--card);
    box-shadow: 0 18px 40px rgba(0,0,0,.55);
    overflow: hidden;
  }
  .card--front { top: 70px; }
  .card--back { top: 520px; }

  .band-rose {
    position: absolute; left: 0; bottom: 0;
    width: 62%; height: 12px; background: var(--rose);
  }
  .band-taupe {
    position: absolute; right: 0; bottom: 0;
    width: 38%; height: 34px; background: var(--taupe);
  }
  .band-taupe::before {
    content: ""; position: absolute; left: 0; top: 0;
    width: 4px; height: 100%; background: var(--card);
  }

  .brand {
    position: absolute;
    display: flex; align-items: center; gap: 16px;
    color: var(--rose);
  }
  .brand__mark {
    width: 40px; height: 40px;
    border: 2px solid var(--rose);
    flex: none;
  }
  .brand__name {
    font-size: 38px; font-weight: 400; letter-spacing: 1px; white-space: nowrap;
  }
  .card--front .brand { left: 70px; top: 145px; }
  .card--back .brand { left: 120px; top: 48px; }
  .card--back .brand__name { font-size: 36px; }

  .person { position: absolute; left: 40px; top: 132px; }
  .person__name {
    color: var(--rose); font-size: 22px; font-weight: 500;
    letter-spacing: 1.2px; text-transform: uppercase; line-height: 1; white-space: nowrap;
  }
  .person__title { color: var(--ink-light); font-size: 19px; line-height: 1.2; margin-top: 4px; }

  .divider {
    position: absolute; left: 215px; top: 168px;
    width: 365px; height: 1px; background: var(--rule);
  }

  .contact { position: absolute; left: 40px; top: 212px; list-style: none; }
  .contact li {
    display: flex; align-items: center; gap: 12px;
    color: var(--ink-light); font-size: 17px; line-height: 25px; white-space: nowrap;
  }
  .contact svg { width: 15px; height: 15px; flex: none; }

  .address {
    position: absolute; right: 40px; top: 232px;
    color: var(--ink-light); font-size: 17px; line-height: 22px; text-align: right;
    font-style: normal;
  }
</style>
</head>
<body>

  <section class="card card--front" aria-label="Card front">
    <div class="brand">
      <span class="brand__mark" aria-hidden="true"></span>
      <span class="brand__name">Larkfield Strategy Advisors</span>
    </div>
    <div class="band-rose"></div>
    <div class="band-taupe"></div>
  </section>

  <section class="card card--back" aria-label="Card back">
    <div class="brand">
      <span class="brand__mark" aria-hidden="true"></span>
      <span class="brand__name">Larkfield Strategy Advisors</span>
    </div>

    <div class="person">
      <p class="person__name">Dr. Oscar Teodoro-Lindqvist</p>
      <p class="person__title">Principal Advisor</p>
    </div>
    <div class="divider"></div>

    <ul class="contact">
      <li>
        <svg viewBox="0 0 16 16" aria-hidden="true"><path fill="none" stroke="#c8928a" stroke-width="1.6" d="M4 2l2.5 3-1.5 1.5c.8 1.8 2.2 3.2 4 4L10.5 9l3 2.5-1.5 2C7 13 3 9 2.5 4z"/></svg>
        <span>202.555.0148</span>
      </li>
      <li>
        <svg viewBox="0 0 16 16" aria-hidden="true"><rect x="1.5" y="3.5" width="13" height="9" fill="none" stroke="#c8928a" stroke-width="1.5"/><path d="M1.5 3.5L8 9l6.5-5.5" fill="none" stroke="#c8928a" stroke-width="1.5"/></svg>
        <span>OTL@LarkfieldStrategyAdvisors.com</span>
      </li>
      <li>
        <svg viewBox="0 0 16 16" aria-hidden="true"><g fill="none" stroke="#c8928a" stroke-width="1.3"><circle cx="8" cy="8" r="6.5"/><ellipse cx="8" cy="8" rx="3" ry="6.5"/><path d="M1.5 8h13M2.5 5h11M2.5 11h11"/></g></svg>
        <span>www.larkfieldstrategyadvisors.com</span>
      </li>
    </ul>

    <address class="address">
      845 Alder Row Suite 210<br>
      Washington, DC 20005
    </address>

    <div class="band-rose"></div>
    <div class="band-taupe"></div>
  </section>

</body>
</html>
```